Design a 1-page brochure with our "The Harbinger Pathway" illustrated.

i have included my logo, an outline of the text and name of each step, and a quick sketch of generally how i would like the image to look. But please make it look sexy.

Each step should include the subtext as shown on the pdf attached. i.e. The first part of the image (far left) is "Problems", under that should list : 1. Poor Expectations; 2. Poor Communication... and so on for all the steps included.

I have also included a previous brochure that shows our branding and style.

Target Market(s)

Restaurant, Retail, Commercial

Industry/Entity Type

Construction Management

Font styles to use
Sans Serif

Colors
EB3D1F
EC4F4E
F09395
F8D3D4
FCEDEE

Requirements
Must have
• Our logo. Title of graphic: The Harbinger Pathway, our website and IG. www.quorvanbuildco.example. @quorvanbuildco

```html
<!DOCTYPE html>
<html lang="en">
<head>
<meta charset="utf-8">
<title>The Harbinger Pathway</title>
<link rel="stylesheet" href="https://fonts.googleapis.com/css2?family=Archivo:ital,wght@1,800&family=Montserrat:wght@700;800&family=Questrial&display=swap">
<style>
  :root {
    --paper: #a9a9a9;
    --red: #e8302a;
    --red-deep: #a11f28;
    --rule: #d3262a;
    --panel: #eeefef;
    --ink: #1b1b1b;
    --muted: #3a3a3a;
  }
  * { margin: 0; padding: 0; box-sizing: border-box; }
  html, body { width: 1200px; height: 882px; overflow: hidden; }
  body { background: var(--paper); position: relative; font-family: "Questrial", sans-serif; }

  .frame-rules { position: absolute; inset: 0; width: 1200px; height: 882px; }

  .title-box {
    position: absolute; left: 239px; top: 110px; width: 722px; height: 88px;
    border: 1.5px solid var(--rule); border-radius: 18px;
    display: flex; align-items: center; justify-content: center;
  }
  .title {
    font-family: "Archivo", sans-serif; font-style: italic; font-weight: 800;
    font-size: 50px; color: var(--red); letter-spacing: 0.5px; white-space: nowrap;
  }

  .step { position: absolute; width: 136px; height: 260px; }
  .step-back {
    position: absolute; left: 0; top: 0; width: 136px; height: 175px;
    border-radius: 22px;
    background: linear-gradient(90deg, var(--red) 0%, #c4252a 55%, var(--red-deep) 100%);
  }
  .step-number {
    position: absolute; left: 0; top: 10px; width: 136px; text-align: center;
    font-family: "Questrial", sans-serif; font-size: 42px; color: #fff; line-height: 1;
  }
  .step-panel {
    position: absolute; left: 15px; top: 77px; width: 107px; height: 124px;
    background: var(--panel); border-radius: 10px; padding: 11px 9px 0 9px;
    box-shadow: 0 3px 8px rgba(0,0,0,0.18);
  }
  .step-panel::before {
    content: ""; position: absolute; left: 50%; top: -13px; transform: translateX(-50%);
    border-left: 11px solid transparent; border-right: 11px solid transparent;
    border-bottom: 14px solid var(--panel);
  }
  .step-name {
    font-family: "Montserrat", sans-serif; font-weight: 800; font-size: 10.5px;
    color: var(--red); line-height: 1.2; margin-bottom: 5px;
  }
  .step-list { list-style: none; }
  .step-list li {
    font-size: 5.2px; color: var(--muted); line-height: 1.3; margin-bottom: 5px;
    padding-left: 6px; position: relative;
  }
  .step-list li::before { content: "\2713"; position: absolute; left: 0; }
  .step-icon {
    position: absolute; left: 51px; top: 186px; width: 34px; height: 34px; border-radius: 50%;
    background: radial-gradient(circle at 35% 30%, #f0413a, var(--red-deep));
    box-shadow: 0 4px 7px rgba(0,0,0,0.3);
    display: flex; align-items: center; justify-content: center;
  }
  .step-shadow {
    position: absolute; left: 30px; top: 238px; width: 76px; height: 6px; border-radius: 50%;
    background: radial-gradient(ellipse, rgba(0,0,0,0.22), rgba(0,0,0,0));
  }

  .brand-name {
    position: absolute; left: 65px; top: 803px;
    font-family: "Montserrat", sans-serif; font-weight: 800; font-size: 11.5px;
    color: var(--ink); letter-spacing: 0.3px;
  }
  .brand-mark {
    position: absolute; left: 118px; top: 735px; width: 52px; height: 52px; background: var(--red);
  }
  .website {
    position: absolute; right: 32px; top: 818px; font-size: 13px; letter-spacing: 4.2px; color: var(--ink);
  }
  .website .site-name { color: var(--rule); }
</style>
</head>
<body>
  <svg class="frame-rules" viewBox="0 0 1200 882" aria-hidden="true">
    <polyline points="465,29 1171,29 1171,625" fill="none" stroke="#d3262a" stroke-width="1.5"/>
    <polyline points="28,256 28,852 735,852" fill="none" stroke="#d3262a" stroke-width="1.5"/>
  </svg>

  <div class="title-box"><h1 class="title">THE HARBINGER PATHWAY</h1></div>

  <section class="step" style="left:110px; top:315px;">
    <div class="step-back"></div>
    <div class="step-number">01</div>
    <div class="step-panel">
      <h2 class="step-name">COMMON<br>PROBLEMS</h2>
      <ul class="step-list">
        <li>Changing or poor expectations.</li>
        <li>Poor Communication</li>
        <li>No Journey To Success</li>
        <li>No Trust</li>
        <li>No Accountability</li>
      </ul>
    </div>
    <div class="step-icon"><svg width="20" height="20" viewBox="0 0 20 20" fill="none" stroke="#fff" stroke-width="1.4"><circle cx="10" cy="10" r="8.5"/><path d="M7.3 7.6a2.8 2.8 0 1 1 3.8 2.6c-.8.4-1.1.9-1.1 1.8v.6"/><circle cx="10" cy="14.8" r=".5" fill="#fff"/></svg></div>
    <div class="step-shadow"></div>
  </section>

  <section class="step" style="left:282px; top:374px;">
    <div class="step-back"></div>
    <div class="step-number">02</div>
    <div class="step-panel">
      <h2 class="step-name">ORGANIZE</h2>
      <ul class="step-list">
        <li>Develop Project Plan</li>
        <li>Develop Schedule</li>
        <li>Develop Budget</li>
      </ul>
    </div>
    <div class="step-icon"><svg width="20" height="20" viewBox="0 0 20 20" fill="#fff"><circle cx="10" cy="5" r="2"/><circle cx="4.5" cy="8" r="1.7"/><circle cx="15.5" cy="8" r="1.7"/><path d="M6.5 15a3.5 3.5 0 0 1 7 0z"/><path d="M1.8 13a2.7 2.7 0 0 1 5.4 0z"/><path d="M12.8 13a2.7 2.7 0 0 1 5.4 0z"/></svg></div>
    <div class="step-shadow"></div>
  </section>

  <section class="step" style="left:451px; top:315px;">
    <div class="step-back"></div>
    <div class="step-number">03</div>
    <div class="step-panel">
      <h2 class="step-name">EXECUTE</h2>
      <ul class="step-list"><li>Project Start</li></ul>
    </div>
    <div class="step-icon"><svg width="20" height="20" viewBox="0 0 20 20" fill="none" stroke="#fff" stroke-width="1.3"><circle cx="10" cy="10" r="3"/><path d="M10 2v2.5M10 15.5V18M2 10h2.5M15.5 10H18M4.3 4.3l1.8 1.8M13.9 13.9l1.8 1.8M4.3 15.7l1.8-1.8M13.9 6.1l1.8-1.8"/><circle cx="10" cy="10" r="5.7"/></svg></div>
    <div class="step-shadow"></div>
  </section>

  <section class="step" style="left:613px; top:374px;">
    <div class="step-back"></div>
    <div class="step-number">04</div>
    <div class="step-panel">
      <h2 class="step-name">MANAGE</h2>
      <ul class="step-list">
        <li>O.O.D.A</li>
        <li>Shared Consciousness Meetings</li>
        <li>Pressurized Collaboration</li>
      </ul>
    </div>
    <div class="step-icon"><svg width="20" height="20" viewBox="0 0 20 20" fill="#fff"><circle cx="8" cy="6" r="3"/><path d="M2.5 16a5.5 5.5 0 0 1 9-4.2V16z"/><circle cx="14.5" cy="14" r="3" fill="none" stroke="#fff" stroke-width="1.6"/></svg></div>
    <div class="step-shadow"></div>
  </section>

  <section class="step" style="left:784px; top:315px;">
    <div class="step-back"></div>
    <div class="step-number">05</div>
    <div class="step-panel">
      <h2 class="step-name">COMPLETE</h2>
      <ul class="step-list"><li>Project Closeout</li></ul>
    </div>
    <div class="step-icon"><svg width="20" height="20" viewBox="0 0 20 20" fill="none" stroke="#fff" stroke-width="1.6"><circle cx="10" cy="10" r="8"/><path d="M6 10.2l3 3 6.5-7"/></svg></div>
    <div class="step-shadow"></div>
  </section>

  <section class="step" style="left:953px; top:374px;">
    <div class="step-back"></div>
    <div class="step-number">06</div>
    <div class="step-panel">
      <h2 class="step-name">POSSIBILITY</h2>
      <ul class="step-list">
        <li>Project Synergy.</li>
        <li>Excellent Communication where Budget and Schedule are visible and approved.</li>
        <li>Clear project visibility where everyone understands how we get to a successful end.</li>
        <li>Everyone involved is proud of the final product</li>
      </ul>
    </div>
    <div class="step-icon"><svg width="20" height="20" viewBox="0 0 20 20" fill="none" stroke="#fff" stroke-width="1.2"><circle cx="10" cy="6" r="2.2"/><path d="M6.5 17v-5a3.5 3.5 0 0 1 7 0v5"/><path d="M10 1.5v1M4 4l1 1M16 4l-1 1M2.5 9h1.2M16.3 9h1.2"/></svg></div>
    <div class="step-shadow"></div>
  </section>

  <div class="brand-mark" aria-hidden="true"></div>
  <div class="brand-name">QUORVAN BUILD CO</div>

  <div class="website">www.<span class="site-name">quorvanbuildco</span>.example</div>
</body>
</html>
```